Pulpa&Mix

We need a new menu design for a juice shop called pulpa&Mix

Industry/Entity Type

Shop

Colors
9bcb3c
ffcf3e
ffffff
f04a51

Requirements
Must have
• we want winter version and summer version must have focus on hot drinks and chocolate and there must be images to bring the attention to these items and same as for the summer version, we need new design and fresh look.
• this is our instagram account : pulpaandmix.zq
• you can find pictures and use them or you can download similar pictures with higher resolution.
• and we need to add Turkish coffee 2000LL to the menu.
• i need the green and orange colors to be the main ones.
• size of menu : A4

```html
<!DOCTYPE html>
<html lang="en">
<head>
<meta charset="utf-8">
<title>Pulpa&amp;Mix Menu</title>
<link href="https://fonts.googleapis.com/css2?family=Exo+2:ital,wght@0,500;0,600;1,400;1,500&family=Lobster&display=swap" rel="stylesheet">
<style>
  :root {
    --green: #7cb82f;
    --green-light: #9bcb3c;
    --orange: #f9a51b;
    --yellow: #ffcf3e;
    --red: #f04a51;
    --ink: #1b1b1b;
    --paper: #ffffff;
    --stage: #1e1e1e;
  }
  * { margin: 0; padding: 0; box-sizing: border-box; }
  html, body { width: 1200px; height: 1200px; overflow: hidden; background: var(--stage); }
  .spread {
    position: absolute; left: 40px; top: 201px; width: 1120px; height: 798px;
    display: flex; background: var(--paper);
  }
  .page { position: relative; width: 560px; height: 798px; overflow: hidden; }
  .page--menu { background: var(--paper); }
  .page--cover {
    background: radial-gradient(circle at 50% 55%, #ffffff 0%, #f4f4f4 60%, #ececec 100%);
    box-shadow: inset 18px 0 22px -14px rgba(0,0,0,0.18);
  }

  .section { position: absolute; left: 0; width: 100%; }
  .section__ribbon {
    display: block; width: 171px; height: 30px; background: var(--orange);
    clip-path: polygon(0 0, 100% 0, 93% 50%, 100% 100%, 0 100%);
    font-family: "Lobster", cursive; font-size: 19px; color: var(--ink);
    line-height: 30px; padding-left: 46px;
  }
  .items { list-style: none; margin-top: 14px; }
  .item {
    display: flex; align-items: baseline; height: 19.6px;
    font-family: "Exo 2", sans-serif; font-style: italic; font-size: 13.5px; color: var(--ink);
    padding-left: 44px;
  }
  .item__name { white-space: nowrap; }
  .item__dots { flex: 0 1 auto; width: 100%; border-bottom: 1px dotted #555; margin: 0 4px 3px; min-width: 6px; }
  .item__price {
    flex: 0 0 auto; width: 120px; font-style: normal; font-weight: 500; color: var(--green); font-size: 13.5px;
  }
  .item--plain { padding-right: 0; }

  .footer-rule { position: absolute; left: 0; top: 680px; width: 100%; height: 8px; background: var(--green); }
  .footer {
    position: absolute; left: 0; top: 688px; width: 100%; height: 110px; background: var(--orange);
    font-family: "Exo 2", sans-serif; font-weight: 600; color: #2b1a00; font-size: 14px; letter-spacing: 0.6px;
    text-align: center;
  }
  .footer__address { margin-top: 28px; }
  .footer__social { margin-top: 14px; display: flex; justify-content: center; gap: 38px; align-items: center; }
  .footer__social span { display: inline-flex; align-items: center; gap: 8px; }
  .footer__mark { width: 10px; height: 10px; background: #2b1a00; display: inline-block; }

  .brand {
    position: absolute; left: 0; top: 96px; width: 100%; display: flex; justify-content: center; align-items: center; gap: 12px;
    font-family: "Exo 2", sans-serif; font-weight: 600; font-size: 40px; color: var(--green-light);
  }
  .brand__dot { width: 22px; height: 22px; border-radius: 50%; background: var(--orange); }
  .hero {
    position: absolute; left: 44px; top: 252px; width: 460px; height: 448px;
    background: radial-gradient(ellipse at 50% 60%, #ffb63a 0%, #f7c84a 30%, #f36b5c 55%, #a6d24c 78%, rgba(255,255,255,0) 100%);
    border-radius: 12px;
  }
  .order {
    position: absolute; left: 83px; top: 728px; width: 421px; height: 40px; background: var(--orange);
    font-family: "Exo 2", sans-serif; font-weight: 500; font-size: 19px; color: #2b1a00;
    text-align: center; line-height: 40px;
  }
</style>
</head>
<body>
<main class="spread">
  <section class="page page--menu">
    <div class="section" style="top:26px">
      <span class="section__ribbon">Gym Lovers</span>
      <ul class="items">
        <li class="item"><span class="item__name">Straw bery Shake</span><span class="item__dots"></span><span class="item__price">6000 L.L</span></li>
        <li class="item"><span class="item__name">Banana Shake</span><span class="item__dots"></span><span class="item__price">7000 L.L</span></li>
        <li class="item"><span class="item__name">Avocado Shake</span><span class="item__dots"></span><span class="item__price">6000 L.L</span></li>
        <li class="item"><span class="item__name">Protein Shake</span><span class="item__dots"></span><span class="item__price">5000 L.L</span></li>
        <li class="item"><span class="item__name">Protein Pancake</span><span class="item__dots"></span><span class="item__price">7000 L.L</span></li>
      </ul>
    </div>

    <div class="section" style="top:188px">
      <span class="section__ribbon">Detox Juices</span>
      <ul class="items">
        <li class="item"><span class="item__name">Red</span><span class="item__dots"></span><span class="item__price">6000 L.L</span></li>
        <li class="item"><span class="item__name">Green</span><span class="item__dots"></span><span class="item__price">7000 L.L</span></li>
      </ul>
    </div>

    <div class="section" style="top:284px">
      <span class="section__ribbon">Sally Crepes</span>
      <ul class="items">
        <li class="item"><span class="item__name">Sugar+ Butter</span><span class="item__dots"></span><span class="item__price">3000 L.L</span></li>
        <li class="item"><span class="item__name">Nutoza</span><span class="item__dots"></span><span class="item__price">5000 L.L</span></li>
        <li class="item"><span class="item__name">Nutoza + banana + Nuts</span><span class="item__dots"></span><span class="item__price">6000 L.L</span></li>
        <li class="item"><span class="item__name">Velora White Chocolate</span><span class="item__dots"></span><span class="item__price">5000 L.L</span></li>
        <li class="item"><span class="item__name">Minka Chocolate</span><span class="item__dots"></span><span class="item__price">5000 L.L</span></li>
        <li class="item"><span class="item__name">Chocolate + Nuts + 1 Vanilla ice cream scoop</span><span class="item__dots"></span><span class="item__price">9000 L.L</span></li>
        <li class="item"><span class="item__name">Protein Pancake</span><span class="item__dots"></span><span class="item__price">10.000 L.L</span></li>
        <li class="item"><span class="item__name">ettucini + Belgian Chocolate +</span><span class="item__dots" style="border:0"></span><span class="item__price">6000 L.L</span></li>
        <li class="item"><span class="item__name">Nuts 1 Vanilla ice cream scoop</span><span class="item__dots"></span><span class="item__price">5000 L.L</span></li>
        <li class="item"><span class="item__name">Velora White Chocolate</span><span class="item__dots"></span><span class="item__price">5000 L.L</span></li>
        <li class="item"><span class="item__name">Minka Chocolate</span><span class="item__dots"></span><span class="item__price">9000 L.L</span></li>
        <li class="item"><span class="item__name">Chocolate + Nuts + 1 Vanilla ice cream scoop</span><span class="item__dots"></span><span class="item__price">10.000 L.L</span></li>
      </ul>
    </div>

    <div class="section" style="top:567px">
      <span class="section__ribbon" style="width:185px">Any Toppings?</span>
      <ul class="items">
        <li class="item"><span class="item__name">Fruits, Marchmallow, Nuts, Sprinkos.</span></li>
        <li class="item"><span class="item__name">Loma cream, Cocoa biscuits, Peanut butter</span><span class="item__dots"></span><span class="item__price">1000 L.L</span></li>
        <li class="item"><span class="item__name">Turkish coffee</span><span class="item__dots"></span><span class="item__price">2000L.L</span></li>
      </ul>
    </div>

    <div class="footer-rule"></div>
    <footer class="footer">
      <p class="footer__address">Birhaven - Tel: 04/512608 - 71/640275 I Corlon - Tel: 01/735914</p>
      <p class="footer__social">
        <span><i class="footer__mark"></i>pulpaandmix.zq</span>
        <span>I</span>
        <span><i class="footer__mark"></i>pulpaandmix</span>
      </p>
    </footer>
  </section>

  <section class="page page--cover">
    <div class="brand"><span class="brand__dot"></span>Pulpa&amp;Mix</div>
    <div class="hero" role="img" aria-label="Glasses of green, red, orange and lemon juice with sliced grapefruit, orange, lemon and lime"></div>
    <div class="order">Order Now on 04/512608 &nbsp;I&nbsp; 71/640275</div>
  </section>
</main>
</body>
</html>
```